Web page design for technology solution company
Velmork Inc.
Dear PH,
Kindly star rate #83 it will help me to go through.
Thanks!
Hi PH,
Any feedback for #52
Thanks
Kindly check your private messages.
#57 and #58 - don't need the extra info. Stick with your earlier versions - like those better. They're simple and not 'overloaded'
#55, #56 - like the simplicity but don't like the dark background
Hi PH, please check your private message. thanks
#13 and #19 - can we see the design without the graphics?
#20 -#24 - much better with the lighter background!
@PH
Kindly check your private message box on the top right & reply asap with your feedback.Thanks
#10 - #12. They seem interesting but on the darker side. Can we see them with a white background?
#9 - Nice and clean design. It's unique and colors are nicely coordinated. Can you find a place for social media icons?
#1 - #5 . Some of the designs look interesting but the background is too dark. Can we see the same with white background?
PH please check your private message
Perin Koldesh

```html
<!DOCTYPE html>
<html lang="en">
<head>
<meta charset="utf-8">
<title>Velmork Inc.</title>
<link rel="stylesheet" href="https://fonts.googleapis.com/css2?family=Oswald:wght@400;500&family=Open+Sans:wght@400&display=swap">
<style>
  :root {
    --page-light: #f7f7f7;
    --page-mid: #e6e6e6;
    --band-shadow: rgba(0,0,0,0.12);
    --logo-grey: #5a5a5a;
    --brand-green: #7cb82f;
    --text-dark: #4a4a4a;
    --text-soft: #6f6f6f;
    --footer-bg: #e9e9e9;
    --footer-line: #d4d4d4;
    --social-dark: #4d4d4d;
    --tab-label: #ffffff;
  }
  * { margin: 0; padding: 0; box-sizing: border-box; }
  html, body { width: 1200px; height: 643px; overflow: hidden; }
  body {
    position: relative;
    font-family: "Open Sans", sans-serif;
    background: radial-gradient(ellipse at 50% 40%, #fbfbfb 0%, var(--page-mid) 75%, #dcdcdc 100%);
  }
  .site-header {
    position: absolute; left: 0; top: 0; width: 1200px; height: 206px;
    background: linear-gradient(to bottom, #fdfdfd 0%, var(--page-light) 60%, #efefef 100%);
    box-shadow: 0 6px 14px var(--band-shadow);
    z-index: 1;
  }
  .brand {
    position: absolute; top: 66px; left: 0; width: 100%;
    display: flex; justify-content: center; align-items: center; gap: 14px;
  }
  .brand-dot { width: 46px; height: 46px; border-radius: 50%; background: var(--brand-green); }
  .brand-name {
    font-family: "Oswald", sans-serif; font-weight: 400; font-size: 52px;
    color: var(--logo-grey); letter-spacing: 1px; line-height: 1;
  }
  .main-nav { position: absolute; top: 200px; left: 0; width: 100%; height: 200px; z-index: 2; }
  .nav-tab { position: absolute; top: 0; width: 144px; height: 190px; text-decoration: none; }
  .nav-tab svg { position: absolute; inset: 0; }
  .nav-tab span {
    position: absolute; top: 86px; left: 0; width: 100%; text-align: center;
    font-family: "Oswald", sans-serif; font-weight: 500; font-size: 21px;
    color: var(--tab-label); text-shadow: 0 1px 2px rgba(0,0,0,0.35);
  }
  .tab-about { left: 266px; }
  .tab-products { left: 545px; }
  .tab-contact { left: 823px; }
  .tagline { position: absolute; top: 456px; left: 0; width: 100%; text-align: center; }
  .tagline-main { font-size: 22px; color: var(--text-dark); }
  .tagline-sub { margin-top: 6px; font-size: 13px; color: var(--text-soft); }
  .site-footer {
    position: absolute; left: 0; bottom: 0; width: 1200px; height: 60px;
    background: var(--footer-bg); border-top: 1px solid var(--footer-line);
  }
  .footer-brand {
    position: absolute; left: 196px; top: 16px;
    font-family: "Oswald", sans-serif; font-size: 22px; color: #9a9a9a; line-height: 1;
  }
  .copyright {
    position: absolute; left: 0; width: 100%; top: 22px; text-align: center;
    font-size: 11px; color: var(--text-dark);
  }
  .social-links { position: absolute; left: 897px; top: 12px; display: flex; gap: 6px; }
  .social-links a { width: 34px; height: 34px; border-radius: 50%; background: var(--social-dark); display: block; }
</style>
</head>
<body>
  <header class="site-header">
    <div class="brand">
      <div class="brand-dot"></div>
      <div class="brand-name">Velmork Inc.</div>
    </div>
  </header>

  <svg width="0" height="0" style="position:absolute">
    <defs>
      <linearGradient id="tab-lime" x1="0" y1="0" x2="1" y2="0">
        <stop offset="0" stop-color="#6fae1c"/><stop offset="0.5" stop-color="#a4da3c"/><stop offset="1" stop-color="#6aa81a"/>
      </linearGradient>
      <linearGradient id="tab-forest" x1="0" y1="0" x2="1" y2="0">
        <stop offset="0" stop-color="#1f7a1f"/><stop offset="0.5" stop-color="#3faa35"/><stop offset="1" stop-color="#1c721c"/>
      </linearGradient>
      <linearGradient id="tab-grass" x1="0" y1="0" x2="1" y2="0">
        <stop offset="0" stop-color="#268226"/><stop offset="0.5" stop-color="#4cb640"/><stop offset="1" stop-color="#237a22"/>
      </linearGradient>
      <linearGradient id="tab-gloss" x1="0" y1="0" x2="0" y2="1">
        <stop offset="0" stop-color="#fff" stop-opacity="0.35"/><stop offset="0.45" stop-color="#fff" stop-opacity="0.05"/><stop offset="1" stop-color="#000" stop-opacity="0.12"/>
      </linearGradient>
    </defs>
  </svg>

  <nav class="main-nav">
    <a class="nav-tab tab-about" href="#about">
      <svg viewBox="0 0 144 190" width="144" height="190" aria-hidden="true">
        <path d="M4 0 H140 V150 L72 184 L4 150 Z" fill="url(#tab-lime)"/>
        <path d="M4 0 H140 V150 L72 184 L4 150 Z" fill="url(#tab-gloss)"/>
        <path d="M8 158 L72 190 L136 158" fill="none" stroke="rgba(0,0,0,0.12)" stroke-width="3"/>
      </svg>
      <span>ABOUT US</span>
    </a>
    <a class="nav-tab tab-products" href="#products">
      <svg viewBox="0 0 144 190" width="144" height="190" aria-hidden="true">
        <path d="M4 0 H140 V150 L72 184 L4 150 Z" fill="url(#tab-forest)"/>
        <path d="M4 0 H140 V150 L72 184 L4 150 Z" fill="url(#tab-gloss)"/>
        <path d="M8 158 L72 190 L136 158" fill="none" stroke="rgba(0,0,0,0.12)" stroke-width="3"/>
      </svg>
      <span>PRODUCTS</span>
    </a>
    <a class="nav-tab tab-contact" href="#contact">
      <svg viewBox="0 0 144 190" width="144" height="190" aria-hidden="true">
        <path d="M4 0 H140 V150 L72 184 L4 150 Z" fill="url(#tab-grass)"/>
        <path d="M4 0 H140 V150 L72 184 L4 150 Z" fill="url(#tab-gloss)"/>
        <path d="M8 158 L72 190 L136 158" fill="none" stroke="rgba(0,0,0,0.12)" stroke-width="3"/>
      </svg>
      <span>CONTACT</span>
    </a>
  </nav>

  <section class="tagline">
    <p class="tagline-main">We provide branded online and mobile platforms and service solutions</p>
    <p class="tagline-sub">that enable and enhance eCommerce and other online interactions for individuals and businesses.</p>
  </section>

  <footer class="site-footer">
    <div class="footer-brand">Velmork Inc.</div>
    <p class="copyright">Copyright © 2012 Velmork Inc. All Rights Reserved.</p>
    <div class="social-links">
      <a href="#" aria-label="Social profile one"></a>
      <a href="#" aria-label="Social profile two"></a>
      <a href="#" aria-label="Social profile three"></a>
    </div>
  </footer>
</body>
</html>
```